Useable Postcard Gift for Artistic Convention Use

Useable Postcard Gift Conference Use, search for web designers
Name of the Company is: Lanternfield Collective
I have an image that I would like to use for the front of the card
along with a by line which says "Let Each Step Lighten the Road Ahead"
Regarding image, i am good to leave the black behind.... should the designer choose. I also have a black and white image to use as well if someone needs it.

Design Target Market: State of the Art, Hip, Elegant, Conscious

This card will be used at a state of the art tech Brindle Summit in Los Angeles. We want to hand it out to those we are interested in continuing relationship with for the purpose of building a website that is comprehensive. We are looking for designers and tech builders for the site.

This is a service business. I would like to have 3 names and titles on the back of the card and a small paragraph of copy. I like the beauty of the postcard i have saved on my account. I like Copper Gothic, thin lettering and Amazone or Caligraphy where it fits.... if it fits.

I want the card to communicate interest in Lanternfield Collective as a state of the art web community that services those progressive professionals who are interested in personal balance and who want to purchase products that are essential to a healthful life.
Updates

Project Deadline Extended
Reason: The deadline is extended through tomorrow due to the need to complete a design. Please continue support

Target Market(s)

High profile clients for coaching, web designers and web technicians for elaborate website build.

Industry/Entity Type

Progressive

Font styles to use
Serif
Script

Colors
00a88f
0555a3
6b449b
ffc214
9bcb3b
f37022

Requirements
Nice to have
• This was supposed to be the must have feature but it wouldn't return there so-----
We want the card to be elegant and definitely a useable postcard.

```html
<!DOCTYPE html>
<html lang="en">
<head>
<meta charset="utf-8">
<title>Lanternfield Collective — Postcard</title>
<link href="https://fonts.googleapis.com/css2?family=Great+Vibes&family=Cinzel:wght@400&display=swap" rel="stylesheet">
<style>
  :root {
    --paper: #ffffff;
    --frame: #1a1a1a;
    --script-green: #66e600;
    --brand-orange: #f7941d;
    --rule: #111111;
    --earth-blue: #0a4fd6;
    --ray-red: #ff1a00;
    --ray-orange: #ff8a00;
    --ray-yellow: #ffe000;
    --ray-green: #33e000;
    --ray-cyan: #00c8f0;
    --ray-violet: #3a1ad8;
  }
  html, body {
    margin: 0;
    padding: 0;
    width: 920px;
    height: 1200px;
    overflow: hidden;
    background: var(--paper);
  }
  .postcard {
    position: relative;
    width: 920px;
    height: 1200px;
    box-sizing: border-box;
    border: 2px solid var(--frame);
    background: var(--paper);
  }
  .sunburst-artwork {
    position: absolute;
    left: 40px;
    top: 30px;
    width: 840px;
    height: 840px;
  }
  .byline {
    position: absolute;
    left: 0;
    right: 0;
    top: 905px;
    margin: 0;
    text-align: center;
    font-family: "Great Vibes", cursive;
    font-weight: 400;
    font-size: 66px;
    line-height: 78px;
    color: var(--script-green);
  }
  .byline-line { display: block; }
  .divider {
    position: absolute;
    left: 160px;
    width: 582px;
    top: 1091px;
    height: 0;
    border-top: 2px solid var(--rule);
  }
  .company-name {
    position: absolute;
    left: 0;
    right: 0;
    top: 1108px;
    margin: 0;
    text-align: center;
    font-family: "Cinzel", serif;
    font-weight: 400;
    font-size: 34px;
    letter-spacing: 1px;
    color: var(--brand-orange);
  }
</style>
</head>
<body>
  <main class="postcard">
    <svg class="sunburst-artwork" viewBox="0 0 840 840" role="img"
         aria-label="Illustration: a rainbow sunburst of meditating and dancing figures radiating around a blue and green globe">
      <defs>
        <radialGradient id="sunburstGlow" cx="50%" cy="50%" r="50%">
          <stop offset="0%"  stop-color="var(--earth-blue)"/>
          <stop offset="22%" stop-color="var(--earth-blue)"/>
          <stop offset="24%" stop-color="var(--ray-red)"/>
          <stop offset="42%" stop-color="var(--ray-orange)"/>
          <stop offset="56%" stop-color="var(--ray-yellow)"/>
          <stop offset="68%" stop-color="var(--ray-green)"/>
          <stop offset="82%" stop-color="var(--ray-cyan)"/>
          <stop offset="94%" stop-color="var(--ray-violet)" stop-opacity="0.6"/>
          <stop offset="100%" stop-color="var(--ray-violet)" stop-opacity="0"/>
        </radialGradient>
      </defs>
      <circle cx="420" cy="420" r="415" fill="url(#sunburstGlow)"/>
    </svg>

    <p class="byline">
      <span class="byline-line">Let Each Step</span>
      <span class="byline-line">Lighten the Road Ahead</span>
    </p>

    <div class="divider"></div>

    <h1 class="company-name">Lanternfield Collective</h1>
  </main>
</body>
</html>
```